Chill Bo
frozen yogurt and more
Corporate
Tara Kessler
Owner
4182 Larkspur Ln.
Columbus IN. 47358
tarasglow@quillpost.com
Don't have store open yet so have no address or phone numbers. We want logo font the same but would like a standard clean font for the rest of the info

```html
<!DOCTYPE html>
<html lang="en">
<head>
<meta charset="utf-8">
<title>Chill Bo – Business Card</title>
<link rel="stylesheet" href="https://fonts.googleapis.com/css2?family=Open+Sans:wght@400;600;700&display=swap">
<style>
  :root {
    --page-bg: #efe7da;
    --card-white: #ffffff;
    --cocoa: #5a3418;
    --leaf-green: #7dbb2e;
    --ink: #3a2a1e;
    --shadow: rgba(60, 40, 20, 0.22);
  }
  * { box-sizing: border-box; margin: 0; padding: 0; }
  html, body {
    width: 1200px;
    height: 780px;
    overflow: hidden;
    background: var(--page-bg);
    font-family: "Open Sans", Arial, sans-serif;
  }
  .stage {
    width: 1200px;
    height: 780px;
    display: flex;
    align-items: center;
    justify-content: center;
  }
  .business-card {
    position: relative;
    width: 1050px;
    height: 600px;
    background: var(--card-white);
    border-radius: 34px;
    overflow: hidden;
    box-shadow: 0 10px 30px var(--shadow);
  }
  .edge-band {
    position: absolute;
    left: 0; top: 0; bottom: 0;
    width: 64px;
    background: var(--cocoa);
  }
  .edge-rule {
    position: absolute;
    left: 72px; top: 0; bottom: 0;
    width: 4px;
    background: var(--leaf-green);
  }
  .card-content {
    position: absolute;
    left: 76px; right: 0; top: 0; bottom: 0;
    display: flex;
    flex-direction: column;
    align-items: center;
    text-align: center;
  }
  .brand {
    margin-top: 80px;
    display: flex;
    flex-direction: column;
    align-items: center;
  }
  .brand-name-row {
    display: flex;
    align-items: center;
    gap: 22px;
  }
  .brand-dot {
    width: 34px;
    height: 34px;
    border-radius: 50%;
    background: var(--leaf-green);
  }
  .brand-name {
    font-size: 96px;
    font-weight: 400;
    color: var(--cocoa);
    line-height: 1;
    letter-spacing: 1px;
  }
  .brand-tagline {
    margin-top: 14px;
    font-size: 28px;
    font-weight: 400;
    letter-spacing: 6px;
    color: var(--leaf-green);
    text-transform: uppercase;
  }
  .contact {
    margin-top: 64px;
    display: flex;
    flex-direction: column;
    align-items: center;
    gap: 12px;
    color: var(--ink);
  }
  .person {
    font-size: 34px;
    line-height: 1.2;
  }
  .person-name { font-weight: 700; color: var(--cocoa); }
  .person-divider { font-weight: 700; color: var(--cocoa); margin: 0 8px; }
  .person-role { font-weight: 600; color: var(--leaf-green); font-size: 26px; }
  .contact-line {
    font-size: 24px;
    line-height: 1.35;
  }
  .contact-address { margin-top: 10px; }
</style>
</head>
<body>
  <main class="stage">
    <article class="business-card">
      <div class="edge-band"></div>
      <div class="edge-rule"></div>
      <div class="card-content">
        <header class="brand">
          <div class="brand-name-row">
            <span class="brand-dot"></span>
            <span class="brand-name">Chill Bo</span>
          </div>
          <p class="brand-tagline">Frozen Yogurt and More</p>
        </header>
        <section class="contact">
          <p class="person">
            <span class="person-name">Tara Kessler</span><span class="person-divider">/</span><span class="person-role">Owner</span>
          </p>
          <p class="contact-line">tarasglow@quillpost.com</p>
          <p class="contact-line contact-address">4182 Larkspur Ln. Columbus IN. 47358</p>
        </section>
      </div>
    </article>
  </main>
</body>
</html>
```